Harborline Realty Property Management Team

We’re going to send out post cards to our neighborhood to potential Investment Property Owners to inform them about our Property Management Services. Looking for something clear, simple, easy to read, not too busy, gets straight to the point. Here’s some verbiage we’d be looking to include, open to different arrangements and ideas.
FREE Property Management for your first 2 months! OR
Your first 2 months of Property Management are FREE!
Get peace of mind with the Harborline Realty way! We lease your property faster and for maximum rent!
Professional Services at the Highest Standard:
• Securing Qualified Tenants
• Collection of Rents
• Managing Maintenance & Repairs
• Staying Current with Rental Laws
• Tenant Management
• Distributing Financial Reports
• Manage & Pay Bills
• Income Property Purchases & Sales
With over 30 years of combined experience we help our Owners reduce liability by using all the proper lease and disclosure contracts and staying current with Rental Laws.
We use advanced technology systems to help:
• Respond faster & provide better services to both owners and tenants.
• Address property maintenance issues faster.
• Process payments faster & more securely.
• Allow our tenants to pay rent online.
• Market your properties & fill vacancies sooner.
• Email statements directly to you as well as have them available at any time.
Our Executive Property Management Team:
Tobias R. Whitfield, Broker/Sr. Property Manager
Marco Teroa, Sr. Property Manager, “Yo Halbo Espanol”
Nadia Pruett, Office Manager
Harborline Realty, Inc.
482 W. 7th Ave., Suite 215
Marlow Bay, CA 90000
Office: (555) 274-9081
Cell (555) 638-1207
www.HarborlineRealty.example
DRE #04927716
Note: feel free to get rid of the background of our Team Photo if that works better, hopefully it's set up to easily clear that out if needed. I attached full and reduced versions in case one or the other is preferred.
Target Market(s)
Investors, property owners, San Luis Obispo County, CA, USA
Industry/Entity Type
Property Management
Colors
Designer to choose colors to be used in the design.
Look and feel

```html
<!DOCTYPE html>
<html lang="en">
<head>
<meta charset="utf-8">
<title>Harborline Realty – Property Management Postcard</title>
<link href="https://fonts.googleapis.com/css2?family=Roboto:wght@400;500;700;900&family=Roboto+Condensed:wght@400;700&display=swap" rel="stylesheet">
<style>
  :root{
    --purple:#4b2a83;
    --purple-dark:#3a1f69;
    --green:#1f7a3a;
    --charcoal:#3b3b3b;
    --ink:#333333;
    --paper:#ffffff;
    --stage:#e9e9e9;
    --rule:#b9b9b9;
  }
  *{box-sizing:border-box;margin:0;padding:0}
  html,body{width:1200px;height:900px;overflow:hidden}
  body{background:var(--stage);font-family:"Roboto",Arial,sans-serif;color:var(--ink);position:relative}
  .postcard{position:absolute;top:260px;width:570px;height:380px;background:var(--paper);overflow:hidden;box-shadow:0 4px 14px rgba(0,0,0,.18)}
  .postcard--front{left:20px}
  .postcard--back{left:610px}
  .layer{position:absolute;inset:0}
  .brand{display:flex;align-items:center;gap:5px;font-family:"Roboto",Arial,sans-serif;font-weight:900;color:var(--green);white-space:nowrap}
  .brand__dot{width:9px;height:9px;border-radius:50%;background:var(--green);flex:none}

  /* front */
  .front__brand{position:absolute;left:14px;top:200px;font-size:17px}
  .front__title{position:absolute;left:14px;top:238px;font-family:"Roboto Condensed",Arial,sans-serif;color:var(--ink)}
  .front__title-small{display:block;font-size:16px;font-weight:400;line-height:1.1}
  .front__title-big{display:block;font-size:34px;font-weight:700;color:var(--purple);line-height:1.05}
  .front__call{position:absolute;left:0;bottom:0;width:185px;height:38px;background:var(--charcoal);color:#fff;font-size:12px;display:flex;align-items:center;padding-left:14px;font-family:"Roboto Condensed",Arial,sans-serif}

  /* back */
  .back__stamp{position:absolute;right:40px;top:22px;width:50px;height:56px;border:1.5px solid var(--rule)}
  .back__brand{position:absolute;left:380px;top:40px;font-size:10px}
  .back__lines{position:absolute;left:360px;top:110px;width:170px}
  .back__lines span{display:block;height:1px;background:var(--rule);margin-bottom:17px}
  .offer{position:absolute;left:232px;top:36px;width:78px;height:78px;border-radius:50%;border:3px solid var(--green);background:#fff;text-align:center;display:flex;flex-direction:column;align-items:center;justify-content:center;line-height:1.05}
  .offer__free{font-size:17px;font-weight:900;color:var(--green)}
  .offer__text{font-size:6.5px;color:var(--ink);margin-top:2px;width:58px}
  .offer__text b{color:var(--green)}
  .back__body{position:absolute;left:22px;top:160px;width:330px;font-size:6.6px;line-height:1.35}
  .team__heading{font-size:9px;font-weight:700;color:var(--ink)}
  .team__names{margin-top:2px;font-weight:500}
  .section__heading{font-size:10px;font-weight:700;color:var(--purple);margin-top:7px;margin-bottom:2px}
  .list-cols{display:grid;grid-template-columns:1fr 1fr;column-gap:14px}
  .list-cols ul{list-style:none}
  .list-cols li{padding-left:7px;position:relative}
  .list-cols li::before{content:"";position:absolute;left:0;top:3px;width:3px;height:3px;background:var(--purple);border-radius:50%}
  .contact{position:absolute;left:0;right:0;bottom:0;height:42px;color:#fff;font-size:7.5px}
  .contact__item{position:absolute;display:flex;align-items:center;gap:4px;white-space:nowrap}
  .contact__item svg{flex:none}
</style>
</head>
<body>

<section class="postcard postcard--front" aria-label="Postcard front">
  <svg class="layer" width="570" height="380" viewBox="0 0 570 380">
    <defs>
      <linearGradient id="houseTone" x1="0" y1="0" x2="0" y2="1">
        <stop offset="0" stop-color="#9fb7cf"/>
        <stop offset="0.45" stop-color="#4f5d78"/>
        <stop offset="0.7" stop-color="#8a8f95"/>
        <stop offset="1" stop-color="#5d8f3a"/>
      </linearGradient>
      <linearGradient id="familyTone" x1="0" y1="0" x2="1" y2="1">
        <stop offset="0" stop-color="#d9b48a"/>
        <stop offset="1" stop-color="#f1ede6"/>
      </linearGradient>
    </defs>
    <rect x="185" y="0" width="385" height="380" fill="url(#houseTone)" role="img" aria-label="Photo of a two-storey blue craftsman house with a stone path and green lawn"/>
    <polygon points="0,0 185,0 185,180 0,105" fill="url(#familyTone)" role="img" aria-label="Photo of a smiling family sitting together under a roof shape"/>
    <line x1="0" y1="105" x2="185" y2="180" stroke="var(--green)" stroke-width="4"/>
    <line x1="185" y1="0" x2="185" y2="380" stroke="var(--green)" stroke-width="4"/>
  </svg>
  <div class="brand front__brand"><span class="brand__dot"></span>Harborline Realty</div>
  <h1 class="front__title">
    <span class="front__title-small">Property Management</span>
    <span class="front__title-big">Services</span>
  </h1>
  <div class="front__call">Call us at: 555-638-1207</div>
</section>

<section class="postcard postcard--back" aria-label="Postcard back">
  <svg class="layer" width="570" height="380" viewBox="0 0 570 380">
    <polygon points="0,0 70,0 0,70" fill="var(--purple)"/>
    <rect x="22" y="38" width="200" height="112" fill="#8ea3b8" role="img" aria-label="Photo of the executive property management team standing in front of a house"/>
    <line x1="300" y1="100" x2="400" y2="330" stroke="var(--green)" stroke-width="3"/>
    <polygon points="0,338 380,338 570,300 570,380 0,380" fill="var(--purple)"/>
  </svg>

  <div class="offer">
    <span class="offer__free">FREE</span>
    <span class="offer__text">Property Management for your first <b>2 Months</b></span>
  </div>

  <div class="back__stamp"></div>
  <div class="brand back__brand"><span class="brand__dot"></span>Harborline Realty</div>
  <div class="back__lines"><span></span><span></span><span></span><span></span></div>

  <div class="back__body">
    <h2 class="team__heading">Our Executive Property Management Team</h2>
    <p class="team__names">Tobias R. Whitfield, Broker/Sr. Property Manager<br>Marco Teroa, Sr. Property Manager, “Yo Halbo Espanol”<br>Nadia Pruett, Office Manager</p>

    <h3 class="section__heading">Services</h3>
    <div class="list-cols">
      <ul>
        <li>Securing Qualified Tenants</li>
        <li>Collection of Rents</li>
        <li>Managing Maintenance &amp; Repairs</li>
        <li>Staying Current with Rental Laws</li>
      </ul>
      <ul>
        <li>Tenant Management</li>
        <li>Distributing Financial Reports</li>
        <li>Manage &amp; Pay Bills</li>
        <li>Income Property Purchases &amp; Sales</li>
      </ul>
    </div>

    <h3 class="section__heading">Technology Systems</h3>
    <div class="list-cols">
      <ul>
        <li>Respond faster &amp; provide better services to both owners and tenants.</li>
        <li>Address property maintenance issues faster.</li>
        <li>Process payments faster &amp; more securely.</li>
      </ul>
      <ul>
        <li>Allow our tenants to pay rent online.</li>
        <li>Market your properties &amp; fill vacancies sooner.</li>
        <li>Email statements directly to you and have them available at any time.</li>
      </ul>
    </div>
  </div>

  <div class="contact">
    <div class="contact__item" style="left:22px;top:9px">
      <svg width="8" height="8" viewBox="0 0 24 24"><path fill="#fff" d="M6.6 10.8a15 15 0 0 0 6.6 6.6l2.2-2.2c.3-.3.7-.4 1-.2 1.1.4 2.3.6 3.6.6.6 0 1 .4 1 1V20c0 .6-.4 1-1 1A17 17 0 0 1 3 4c0-.6.4-1 1-1h3.5c.6 0 1 .4 1 1 0 1.3.2 2.5.6 3.6.1.3 0 .7-.2 1z"/></svg>
      Office: (555) 274-9081
    </div>
    <div class="contact__item" style="left:22px;top:23px">
      <svg width="8" height="8" viewBox="0 0 24 24"><path fill="#fff" d="M6.6 10.8a15 15 0 0 0 6.6 6.6l2.2-2.2c.3-.3.7-.4 1-.2 1.1.4 2.3.6 3.6.6.6 0 1 .4 1 1V20c0 .6-.4 1-1 1A17 17 0 0 1 3 4c0-.6.4-1 1-1h3.5c.6 0 1 .4 1 1 0 1.3.2 2.5.6 3.6.1.3 0 .7-.2 1z"/></svg>
      Cell: (555) 638-1207
    </div>
    <div class="contact__item" style="left:150px;top:9px">
      <svg width="8" height="9" viewBox="0 0 24 24"><path fill="#fff" d="M12 2a7 7 0 0 0-7 7c0 5.2 7 13 7 13s7-7.8 7-13a7 7 0 0 0-7-7zm0 9.5A2.5 2.5 0 1 1 12 6.5a2.5 2.5 0 0 1 0 5z"/></svg>
      482 W. 7th Ave., Suite 215
    </div>
    <div class="contact__item" style="left:162px;top:23px">Marlow Bay, CA 90000 · DRE #04927716</div>
    <div class="contact__item" style="left:410px;top:18px;font-size:8px">www.HarborlineRealty.example</div>
  </div>
</section>

</body>
</html>
```